Super Greens Label for Supplement Bottle

We want to design a front label for a health supplement bottle. The product is called Meadow Twist Chews™. This will be a new product so there is no current website for the product. The focus is on supergreens that taste great and deliver support for energy, digestion, and immune defense.
We want it to be modern, vibrant and appealing.
Bottle size: standard size supplement CLEAR bottle size, with white child resistant cap and the label panel dimensions are 3” x 7”. The label should be primarily white and green, with a touch of red; (see color palettes)/it can also ONLY be white and green. See samples attached.
We are only focused on the front of the bottle design, not on the back, but leave space for the supplement panel and other text on the back.
So the text for the front of the bottle is:
RT Balden's
Meadow Twist Chews™
Super Greens Blend for:
Energy, Digestion, and Immune Support*
60 Gummies | Dietary Supplement
Raspberry Flavor Gummies
Off to side of the label:
Non-GMO
Vegan Friendly
Plant-Based
Gelatin Free
Colors
Designer to choose colors to be used in the design.

```html
<!DOCTYPE html>
<html lang="en">
<head>
<meta charset="utf-8">
<title>Meadow Twist Chews – Front Label</title>
<link href="https://fonts.googleapis.com/css2?family=Big+Shoulders+Display:wght@700;800;900&family=Poppins:wght@300;400;600;700&display=swap" rel="stylesheet">
<style>
  :root {
    --forest: #03593e;
    --emerald: #129467;
    --berry: #c0102a;
    --white: #ffffff;
    --paper: #f5f5f5;
    --ink-green: #03593d;
    --berry-dark: #8e1026;
    --berry-light: #e0405a;
  }
  * { margin: 0; padding: 0; box-sizing: border-box; }
  html, body { width: 1049px; height: 1200px; overflow: hidden; background: var(--paper); }
  .canvas { position: relative; width: 1049px; height: 1200px; }
  .label {
    position: absolute; left: 24px; top: 386px;
    width: 1000px; height: 428px;
    background: var(--forest);
    font-family: "Poppins", sans-serif;
    color: var(--white);
  }
  .name-panel {
    position: absolute; left: 393px; top: 0; width: 213px; height: 256px;
    background: var(--emerald);
    border-radius: 0 0 14px 14px;
  }
  .brand {
    position: absolute; left: 393px; width: 213px; top: 18px; text-align: center;
    font-family: "Poppins", sans-serif; font-size: 11px; font-weight: 600;
    letter-spacing: 1.5px; text-transform: uppercase; line-height: 1;
  }
  .name {
    position: absolute; left: 393px; width: 213px; text-align: center;
    font-family: "Big Shoulders Display", sans-serif; line-height: 1;
    color: var(--white);
  }
  .name-top { top: 40px; font-size: 40px; font-weight: 800; }
  .name-main { top: 82px; font-size: 78px; font-weight: 900; letter-spacing: -1px; }
  .name-bottom { top: 158px; font-size: 40px; font-weight: 800; text-transform: uppercase; }
  .name-bottom sup { font-size: 16px; vertical-align: top; line-height: 1; margin-left: 1px; }
  .flavor-pill {
    position: absolute; left: 386px; top: 205px; width: 227px; height: 31px;
    background: var(--berry); border-radius: 16px;
    font-size: 14px; font-weight: 600; letter-spacing: -0.4px;
    display: flex; align-items: center; justify-content: center;
  }
  .claims {
    position: absolute; left: 281px; top: 74px; width: 67px; height: 279px;
    background: var(--white); border-radius: 6px;
    color: var(--ink-green);
  }
  .claim { position: absolute; left: 0; width: 67px; text-align: center; }
  .claim svg { display: block; margin: 0 auto; width: 27px; height: 27px; }
  .claim span { display: block; font-size: 7.5px; line-height: 10px; margin-top: 5px; }
  .blend-title {
    position: absolute; left: 0; width: 1000px; top: 290px; text-align: center;
    font-size: 11px; font-weight: 600; letter-spacing: -0.3px; text-transform: uppercase;
  }
  .benefits {
    position: absolute; left: 0; width: 1000px; top: 312px; text-align: center;
    font-size: 14.5px; font-weight: 300; letter-spacing: -0.2px; text-transform: uppercase;
  }
  .benefits .sep { margin: 0 6px; }
  .berry-art {
    position: absolute; left: 365px; top: 372px; width: 32px; height: 34px;
    border-radius: 45% 45% 50% 50%;
    background: radial-gradient(circle at 40% 35%, var(--berry-light), var(--berry) 55%, var(--berry-dark));
  }
  .stat {
    position: absolute; top: 368px;
    font-family: "Big Shoulders Display", sans-serif; font-weight: 800;
    font-size: 21px; line-height: 19px; text-transform: uppercase;
  }
  .count { left: 407px; }
  .supplement { left: 558px; }
  .divider { position: absolute; left: 510px; top: 370px; width: 0; height: 38px; border-left: 1px dashed var(--white); }
</style>
</head>
<body>
<div class="canvas">
  <section class="label">
    <div class="name-panel"></div>
    <div class="brand">RT Balden's</div>
    <div class="name name-top">Meadow</div>
    <div class="name name-main">TWIST</div>
    <div class="name name-bottom">Chews<sup>™</sup></div>
    <div class="flavor-pill">Raspberry Flavor Gummies</div>

    <aside class="claims">
      <div class="claim" style="top:24px">
        <svg viewBox="0 0 28 28" fill="none" stroke="currentColor" stroke-width="1.2">
          <circle cx="14" cy="14" r="12.5"/>
          <text x="14" y="16.5" text-anchor="middle" font-size="6.5" font-family="Poppins, sans-serif" fill="currentColor" stroke="none">GMO</text>
          <line x1="6" y1="22" x2="22" y2="6"/>
        </svg>
        <span>NON-GMO</span>
      </div>
      <div class="claim" style="top:84px">
        <svg viewBox="0 0 28 28" fill="none" stroke="currentColor" stroke-width="1.2">
          <circle cx="14" cy="14" r="12.5"/>
          <path d="M10 21 C12 15 15 11 20 8 C19 14 16 17 12 18"/>
          <path d="M12 16 C10 13 9 11 9 9"/>
        </svg>
        <span>VEGAN<br>FRIENDLY</span>
      </div>
      <div class="claim" style="top:150px">
        <svg viewBox="0 0 28 28" fill="none" stroke="currentColor" stroke-width="1.2">
          <circle cx="14" cy="14" r="12.5"/>
          <path d="M14 20 V12"/>
          <path d="M14 13 C11 13 9 11 9 8 C12 8 14 10 14 13 Z"/>
          <path d="M14 13 C17 13 19 11 19 8 C16 8 14 10 14 13 Z"/>
        </svg>
        <span>PLANT-BASED</span>
      </div>
      <div class="claim" style="top:210px">
        <svg viewBox="0 0 28 28" fill="none" stroke="currentColor" stroke-width="1.2">
          <circle cx="14" cy="14" r="12.5"/>
          <path d="M9 17 C9 11 19 11 19 17 Z"/>
          <line x1="8" y1="19" x2="20" y2="19"/>
          <line x1="12" y1="13" x2="12" y2="17"/>
          <line x1="16" y1="13" x2="16" y2="17"/>
        </svg>
        <span>GELATIN FREE</span>
      </div>
    </aside>

    <p class="blend-title">Super Greens Blend For</p>
    <p class="benefits">Energy<span class="sep">|</span>Digestion<span class="sep">|</span>Immune Support*</p>

    <div class="berry-art" role="img" aria-label="Illustration of a ripe raspberry"></div>
    <div class="stat count">60<br>Gummies</div>
    <div class="divider"></div>
    <div class="stat supplement">Dietary<br>Supplement</div>
  </section>
</div>
</body>
</html>
```